Business Card Design for Kidvale (Hires out childrens play areas)

Looking to have a business card designed for a company we just bought. The company rents out childrens play areas.

I have uploaded a couple of examples of the kind of business card style I like. Here are two more examples:

https://quorvastudio.nz/project/bright-romp-branding/
https://imgvaultcdn.com/design_img/8841052/302917/302917_5518203_8841052_b73e19a2_image.jpg

I think a white card will be best due to all the colours in the logo.

Size we require: 3.75" x 2.25" (horizontally orientated) with a 0.125" bleed

Uploaded is two versions of our logo.

Details for the card:
1. My name: Liam Verster
2. Title: Managing Director
3. Phone no: 021 563 417
4. Email: liam@kidvale.co.nz
5. URL: www.kidvale.co.nz
6. Address:
PO Box 318625
Fernlea, Auckland

Let me know if you need anything else.

Target Market(s)

Hospitals, doctors surgeries, bed shops, etc.

Contact Information for Business Card

Details for the card:
1. My name: Liam Verster
3. Phone no: 021 563 417
5. URL: www.kidvale.co.nz
6. Address:
PO Box 318625
Fernlea, Auckland

Requirements
Should not have
• Not too busy.

```html
<!DOCTYPE html>
<html lang="en">
<head>
<meta charset="utf-8">
<title>Kidvale Business Card</title>
<link href="https://fonts.googleapis.com/css2?family=Lato:wght@400;700;900&display=swap" rel="stylesheet">
<style>
  :root {
    --canvas-bg: #e6e9ec;
    --card-white: #ffffff;
    --brand-blue: #1a7fd4;
    --brand-blue-deep: #0d62b8;
    --brand-blue-light: #2fa3ea;
    --accent-orange: #f5a31a;
    --text-dark: #222528;
    --text-white: #ffffff;
  }
  * { box-sizing: border-box; margin: 0; padding: 0; }
  html, body {
    width: 1200px;
    height: 960px;
    overflow: hidden;
    background: var(--canvas-bg);
    font-family: "Lato", sans-serif;
  }
  .sheet {
    width: 1200px;
    height: 960px;
    display: flex;
    flex-direction: column;
    align-items: center;
    justify-content: center;
    gap: 60px;
  }
  .card {
    position: relative;
    width: 600px;
    height: 360px;
    overflow: hidden;
    box-shadow: 0 6px 18px rgba(0, 0, 0, 0.15);
  }

  /* Front */
  .card-front { background: var(--card-white); }
  .card-front .swoosh {
    position: absolute;
    inset: 0;
    width: 100%;
    height: 100%;
  }
  .brand-mark {
    position: absolute;
    display: flex;
    align-items: center;
    gap: 12px;
  }
  .brand-mark .brand-dot {
    width: 30px;
    height: 30px;
    border-radius: 50%;
  }
  .brand-mark .brand-name {
    font-weight: 900;
    font-size: 54px;
    letter-spacing: 1px;
    line-height: 1;
  }
  .card-front .brand-mark { left: 42px; top: 52px; }
  .card-front .brand-dot { background: var(--brand-blue); }
  .card-front .brand-name { color: var(--brand-blue); }

  .address {
    position: absolute;
    left: 50px;
    top: 220px;
    font-size: 17px;
    line-height: 22px;
    color: var(--text-dark);
  }
  .contact-list {
    position: absolute;
    left: 50px;
    top: 282px;
    list-style: none;
    font-size: 17px;
    line-height: 23px;
    color: var(--text-dark);
  }
  .contact-list li { display: flex; align-items: center; gap: 14px; }
  .contact-list svg { width: 13px; height: 13px; flex: none; }

  .person {
    position: absolute;
    right: 28px;
    top: 248px;
    text-align: left;
  }
  .person .name {
    font-size: 19px;
    font-weight: 400;
    color: var(--accent-orange);
  }
  .person .title {
    font-size: 13px;
    color: var(--text-white);
    margin-top: 3px;
  }

  /* Back */
  .card-back {
    background: radial-gradient(ellipse at 45% 35%, var(--brand-blue-light) 0%, var(--brand-blue) 55%, var(--brand-blue-deep) 100%);
    display: flex;
    flex-direction: column;
    align-items: center;
    justify-content: center;
  }
  .card-back .brand-mark { position: static; }
  .card-back .brand-dot { background: var(--text-white); }
  .card-back .brand-name { color: var(--text-white); font-size: 60px; }
  .card-back .web {
    margin-top: 60px;
    font-size: 13px;
    letter-spacing: 2px;
    color: var(--text-white);
  }
</style>
</head>
<body>
<main class="sheet">

  <section class="card card-front" aria-label="Business card front">
    <svg class="swoosh" viewBox="0 0 600 360" preserveAspectRatio="none" aria-hidden="true">
      <path d="M548 0 C546 110 500 190 420 252 C510 195 558 115 562 0 Z" fill="var(--accent-orange)"/>
      <path d="M268 360 C420 300 548 190 572 0 L600 0 L600 360 Z" fill="var(--brand-blue)"/>
    </svg>

    <div class="brand-mark">
      <span class="brand-dot"></span>
      <span class="brand-name">Kidvale</span>
    </div>

    <p class="address">PO Box 318625<br>Fernlea, Auckland</p>

    <ul class="contact-list">
      <li>
        <svg viewBox="0 0 16 16" aria-hidden="true"><path d="M3 1 L6 1 L7 5 L5 6.5 C6 9 7 10 9.5 11 L11 9 L15 10 L15 13 C15 14 14 15 13 15 C6.5 15 1 9.5 1 3 C1 2 2 1 3 1 Z" fill="var(--accent-orange)"/></svg>
        021 563 417
      </li>
      <li>
        <svg viewBox="0 0 16 16" aria-hidden="true"><rect x="1" y="3" width="14" height="10" fill="var(--accent-orange)"/><path d="M1 3 L8 9 L15 3" fill="none" stroke="#fff" stroke-width="1.3"/></svg>
        liam@kidvale.co.nz
      </li>
      <li>
        <svg viewBox="0 0 16 16" aria-hidden="true"><circle cx="8" cy="8" r="7" fill="var(--accent-orange)"/><path d="M1 8 H15 M8 1 C4 5 4 11 8 15 M8 1 C12 5 12 11 8 15" fill="none" stroke="#fff" stroke-width="1"/></svg>
        www.kidvale.co.nz
      </li>
    </ul>

    <div class="person">
      <p class="name">Liam Verster</p>
      <p class="title">Managing Director</p>
    </div>
  </section>

  <section class="card card-back" aria-label="Business card back">
    <div class="brand-mark">
      <span class="brand-dot"></span>
      <span class="brand-name">Kidvale</span>
    </div>
    <p class="web">www.kidvale.co.nz</p>
  </section>

</main>
</body>
</html>
```